Our companies name is The Gilded Ladle and we specialize in craft cupcakes, what I mean by that is that we bake our cupcakes with craft beer and other alcoholic drinks. We are trying to focus on being elegant but at the same time unpretentious. Since we are incorporating beer in our cupcakes we want the business card to have our logo in the front and our information in the back.

Once we select the best design we will provide the contact information to be added. Thank you.

Industry/Entity Type

Business

Font styles to use
Decorative
Script

Requirements
Must have
• Round corners
Should not have
• Square corners

```html
<!DOCTYPE html>
<html lang="en">
<head>
<meta charset="utf-8">
<title>The Gilded Ladle – Business Card</title>
<link href="https://fonts.googleapis.com/css2?family=Federant&family=Tinos&family=Dancing+Script&display=swap" rel="stylesheet">
<style>
  :root {
    --backdrop: #e9e4de;
    --card-black: #050505;
    --card-red: #da1f26;
    --teal: #7fcdc3;
    --teal-soft: #9ed8cf;
  }
  * { margin: 0; padding: 0; box-sizing: border-box; }
  html, body { width: 1200px; height: 1000px; overflow: hidden; }
  body { background: var(--backdrop); position: relative; }

  .card {
    position: absolute;
    left: 260px;
    width: 680px;
    height: 385px;
    border-radius: 22px;
    overflow: hidden;
  }
  .card--front { top: 100px; background: var(--card-black); }
  .card--back { top: 533px; background: var(--card-red); }

  .brand-name {
    font-family: "Federant", serif;
    font-size: 40px;
    color: var(--teal);
    text-transform: uppercase;
    letter-spacing: 1px;
    text-align: center;
    line-height: 1.1;
  }
  .card--front .brand-name {
    position: absolute;
    left: 0; right: 0; top: 50%;
    transform: translateY(-50%);
  }

  .back-panel { position: absolute; inset: 0; }
  .card--back .brand-name {
    position: absolute;
    left: 20px; width: 300px; top: 50%;
    transform: translateY(-50%);
    font-size: 34px;
  }

  .contact {
    position: absolute;
    left: 370px; width: 300px; top: 112px;
    text-align: center;
    color: var(--teal-soft);
  }
  .contact__name {
    font-family: "Federant", serif;
    font-size: 38px;
    letter-spacing: 1px;
    text-transform: uppercase;
    padding-bottom: 6px;
    border-bottom: 3px dotted var(--teal-soft);
    margin: 0 8px 30px;
  }
  .contact__value {
    font-family: "Tinos", serif;
    font-size: 20px;
    line-height: 1;
  }
  .contact__value--email { font-size: 17px; }
  .contact__label {
    font-family: "Dancing Script", cursive;
    font-size: 15px;
    margin: 2px 0 20px;
    letter-spacing: 1px;
  }
</style>
</head>
<body>
  <section class="card card--front">
    <p class="brand-name">The<br>Gilded Ladle</p>
  </section>

  <section class="card card--back">
    <svg class="back-panel" viewBox="0 0 680 385" width="680" height="385" aria-hidden="true">
      <path fill="var(--card-black)" stroke="var(--teal)" stroke-width="3"
        d="M0,0 H282
           Q302,16 303,32 Q304,48 322,64 Q330,80 339,96 Q354,112 352,128
           Q350,144 360,160 Q372,176 363,192 Q352,208 360,224 Q368,240 350,256
           Q334,272 336,288 Q338,304 318,320 Q302,336 298,352 Q296,368 283,385
           H0 Z"/>
    </svg>
    <p class="brand-name">The<br>Gilded Ladle</p>

    <div class="contact">
      <p class="contact__name">Dana Reyes</p>
      <p class="contact__value">[555] 284-7190</p>
      <p class="contact__label">phone</p>
      <p class="contact__value contact__value--email">hello@thegildedladle.com</p>
      <p class="contact__label">email</p>
    </div>
  </section>
</body>
</html>
```